Optometrist/Eye Care Clinic Business card with new logo attached

We are a small, independent eye care clinic in Canada. We have recently updated our logo (as attached), and would like a professional, modern and health care oriented business card to highlight our office details and our optometrist. We'd like to incorporate the blue colours as seen on our logo.

Target Market(s)

demographic: age 35-65 male/female equal

Industry/Entity Type

Health Care

Contact Information for Business Card

Name of clinic: "Amber Hollow Eye Care Optometry"

Font styles to use
Sans Serif

Colors
0355a3

Requirements
Must have
• our website: amberholloweyecare.net
• Dr Selma Okonkwo
• Optometrist
• 312-617 E Larkspur Ave
• Vancouver BC V7R 3P8
• P: 604-555-0193
• E: info@amberholloweyecare.net
Nice to have
• front side: logo/name of clinic as seen on logo attached and website
• backside: logo on the left side, and name/title/address/phone/email

```html
<!DOCTYPE html>
<html lang="en">
<head>
<meta charset="utf-8">
<title>Amber Hollow Eye Care Optometry – Business Card</title>
<link href="https://fonts.googleapis.com/css2?family=Arimo:wght@400;700&display=swap" rel="stylesheet">
<style>
  :root {
    --stage: #e4e4e4;
    --paper: #f7f7f6;
    --navy: #033d5c;
    --ink: #1a1a1a;
    --muted: #5b6770;
    --on-navy: #ffffff;
  }
  * { box-sizing: border-box; margin: 0; padding: 0; }
  html, body {
    width: 1200px; height: 1200px; overflow: hidden;
    background: var(--stage);
    font-family: "Arimo", Arial, sans-serif;
  }
  .sheet {
    width: 1200px; height: 1200px;
    display: flex; flex-direction: column;
    align-items: center; justify-content: center;
    gap: 60px;
  }
  .card {
    width: 840px; height: 480px;
    background: var(--paper);
    box-shadow: 0 4px 14px rgba(0,0,0,0.12);
    position: relative;
    overflow: hidden;
  }

  /* Front */
  .card--front {
    display: flex; flex-direction: column; align-items: center; justify-content: center;
    padding-bottom: 60px;
  }
  .brand-name {
    text-align: center;
    font-weight: 400;
    text-transform: uppercase;
    color: var(--navy);
  }
  .card--front .brand-name {
    width: 360px;
    font-size: 34px; line-height: 1.35; letter-spacing: 0.12em;
  }
  .front-url {
    position: absolute; bottom: 56px; left: 0; right: 0;
    text-align: center; font-size: 19px; color: var(--ink);
  }

  /* Back */
  .card--back { display: flex; }
  .back-identity {
    width: 330px; padding: 70px 36px;
    display: flex; flex-direction: column; align-items: center; justify-content: center;
    gap: 56px;
  }
  .card--back .brand-name {
    width: 220px;
    font-size: 16px; line-height: 1.4; letter-spacing: 0.12em;
  }
  .person { align-self: stretch; }
  .person-name { font-size: 26px; font-weight: 700; color: var(--navy); }
  .person-title { margin-top: 6px; font-size: 15px; color: var(--muted); }
  .back-contact {
    flex: 1; background: var(--navy); color: var(--on-navy);
    padding: 0 50px; display: flex; flex-direction: column; justify-content: center;
    gap: 22px; font-size: 17px; line-height: 1.4;
  }
  .contact-row { display: flex; align-items: flex-start; gap: 18px; }
  .contact-icon { width: 16px; height: 16px; flex: none; margin-top: 3px; }
</style>
</head>
<body>
<main class="sheet">
  <section class="card card--front" aria-label="Card front">
    <p class="brand-name">Amber Hollow Eye Care Optometry</p>
    <p class="front-url">amberholloweyecare.net</p>
  </section>

  <section class="card card--back" aria-label="Card back">
    <div class="back-identity">
      <p class="brand-name">Amber Hollow Eye Care Optometry</p>
      <div class="person">
        <p class="person-name">Dr Selma Okonkwo</p>
        <p class="person-title">Optometrist</p>
      </div>
    </div>
    <div class="back-contact">
      <div class="contact-row">
        <svg class="contact-icon" viewBox="0 0 16 16" aria-hidden="true"><path d="M8 1C5.2 1 3 3.2 3 6c0 3.8 5 9 5 9s5-5.2 5-9c0-2.8-2.2-5-5-5zm0 7a2 2 0 1 1 0-4 2 2 0 0 1 0 4z" fill="currentColor"/></svg>
        <p>312-617 E Larkspur Ave<br>Vancouver BC V7R 3P8</p>
      </div>
      <div class="contact-row">
        <svg class="contact-icon" viewBox="0 0 16 16" aria-hidden="true"><rect x="4" y="1" width="8" height="14" rx="1.5" fill="none" stroke="currentColor" stroke-width="1.6"/><circle cx="8" cy="12.3" r="0.9" fill="currentColor"/></svg>
        <p>P: 604-555-0193</p>
      </div>
      <div class="contact-row">
        <svg class="contact-icon" viewBox="0 0 16 16" aria-hidden="true"><rect x="1" y="3" width="14" height="10" rx="1" fill="none" stroke="currentColor" stroke-width="1.5"/><path d="M1.5 3.8 8 9l6.5-5.2" fill="none" stroke="currentColor" stroke-width="1.5"/></svg>
        <p>E: info@amberholloweyecare.net</p>
      </div>
    </div>
  </section>
</main>
</body>
</html>
```